Australian Brand needs a web designer to create a beautiful, functional website to wow the consumer*

Hi,
Tulvo Brenner Australia Pty. Ltd. Needs a ecom website.

This website is for Tulvo Brenner Australia Pty Ltd and will be used with https://tulvobrenner.com.au

Tulvo Brenner Australia offers very unique innovative products that help solve problems in the horticultural, Aeroponics, Hydroponics, and sustainability space.
inside the Australia & New Zealand market.
Our hero product is the Tulvo Brenner Cloning Machine.
Our company's mission is to help everyday people grow healthy food from home, making them more self-sufficient and reduce pressure on our environment.
We are looking to partner with a designer to create and code a website for a new brand we have secured the licensing for Tulvo Brenner Australia.
We require a mobile device friendly website that complies with Quorbit's current algorithm and SEO requirements.
We prefer clean and easy to navigate with video and images telling most of the story to sell our products.
Below is a link to our US website to help with colors logos etc, however, we believe this site is poorly designed & not pleasing to use as a buyer.
Hope you can offer a better experience?
Regards
Keith
https://tulvobrenner.com/
Updates

Hi please see updated brief. I have extended the submission time.

Target Market(s)

Professionals and enthusiast of all ages in Horticultural, Aeroponics, Hydroponics, Gardening (inc professionals and enthusiast growers of fruit, vegetables, Herbs, flowers, bonsai, additionaly Cannabis however cannabis ia not legal in Australia. just to name a few as well as sustainability space.
Australia & New Zealand market.

Industry/Entity Type

Hydroponic

Coding

Coded - Design and coding required

Number of Pages Required

1 page

Font styles to use
Serif

Requirements
Must have
• Mobile device friendly
Email capture offer process on the landing page,
Ability for us upload videos and images that can be easily shared across all platforms, Product catalog that has the ability to include video, text, and images if required, easy add to cart with the checkout process, Ability to offer up-sell products during check out.
Promo for discount if register to shop now.
Nice to have
• Similar colour to the USA Site www.tulvobrenner.com but more high end and modern

```html
<!DOCTYPE html>
<html lang="en">
<head>
<meta charset="utf-8">
<title>Tulvo Brenner Australia</title>
<link href="https://fonts.googleapis.com/css2?family=Roboto:wght@400;500;700;900&display=swap" rel="stylesheet">
<style>
:root{
  --green:#6cbf45;
  --green-dark:#4e9a2e;
  --blue:#2b6cb3;
  --ink:#222;
  --muted:#666;
  --topbar:#4a8f2c;
  --footer:#0d0d0d;
  --footer-base:#000;
}
*{box-sizing:border-box;margin:0;padding:0}
html,body{width:1200px;height:4308px;overflow:hidden}
body{font-family:'Roboto',Arial,sans-serif;color:var(--ink);background:#fff;position:relative}
.abs{position:absolute}
.btn{display:inline-block;background:var(--blue);color:#fff;font-weight:700;font-size:14px;letter-spacing:.5px;padding:12px 26px;border-radius:3px;text-transform:uppercase}

.topbar{left:0;top:0;width:1200px;height:40px;background:var(--topbar);color:#fff;font-size:13px;display:flex;align-items:center;justify-content:space-between;padding:0 40px}
.topbar nav{display:flex;gap:24px}

.header{left:0;top:40px;width:1200px;height:90px;display:flex;align-items:center;padding:0 40px;background:#fff}
.brand{display:flex;align-items:center;gap:10px;font-weight:700;font-size:16px;color:var(--green-dark);width:300px}
.brand .dot{width:54px;height:54px;border-radius:50%;border:3px solid var(--green)}
.mainnav{display:flex;margin-left:40px}
.mainnav a{font-size:15px;font-weight:500;color:var(--ink);padding:10px 18px;text-decoration:none}
.mainnav a.active{background:var(--green);color:#fff}
.social{margin-left:auto;display:flex;gap:10px}
.social span{width:24px;height:24px;background:var(--green);border-radius:3px}

.hero{left:0;top:130px;width:1200px;height:690px;background:linear-gradient(110deg,#1f3a14 0%,#3f6b25 35%,#6c8f3a 60%,#2d4a1b 100%)}
.hero .shade{position:absolute;inset:0;background:linear-gradient(90deg,rgba(0,0,0,.45),rgba(0,0,0,.1) 60%)}
.hero-text{left:232px;top:318px;color:#fff}
.hero-text .small{font-size:40px;font-weight:700;letter-spacing:1px}
.hero-text .big{font-size:60px;font-weight:900;line-height:1;margin-top:8px}
.hero-text .buy{margin-top:44px;display:inline-block;background:var(--green);color:#fff;font-size:14px;font-weight:700;padding:12px 30px;border-radius:3px}
.dots{left:565px;top:740px;display:flex;gap:12px}
.dots span{width:30px;height:30px;border-radius:50%;background:#fff;opacity:.9}
.dots span+span{background:#222}

.clone-img{left:100px;top:920px;width:480px;height:352px;background:linear-gradient(160deg,#cfe6b0,#7fb24f 60%,#3f6d22)}
.arrow-l,.arrow-r{position:absolute;top:160px;width:26px;height:34px;background:rgba(0,0,0,.35)}
.arrow-l{left:0}.arrow-r{right:0}
.clone-copy{left:600px;top:890px;width:520px}
h2.title{color:var(--green);font-size:38px;font-weight:700;line-height:1.2}
.bullets{list-style:none;margin-top:24px}
.bullets li{font-size:14px;color:var(--muted);line-height:1.6;margin-bottom:18px;padding-left:22px;position:relative}
.bullets li:before{content:"";position:absolute;left:0;top:7px;width:8px;height:8px;background:var(--blue)}

.gallery{left:64px;top:1380px;width:1072px;height:360px;display:flex}
.gallery div{flex:1}
.g1{background:linear-gradient(180deg,#4c7a2b,#2f5318)}
.g2{background:linear-gradient(180deg,#8fbf5a,#5f8f38);position:relative}
.g2 .over{position:absolute;inset:0;background:rgba(108,191,69,.55);display:flex;flex-direction:column;align-items:center;justify-content:center;color:#fff;font-weight:700;font-size:22px;gap:14px}
.g3{background:linear-gradient(180deg,#d8e7c6,#92b86a)}
.g4{background:linear-gradient(180deg,#a7cf74,#5b8e2f)}
.g5{background:linear-gradient(180deg,#79b043,#3e6a1f)}

.acc-title{left:0;top:1810px;width:1200px;text-align:center}
.acc-copy{left:64px;top:1955px;width:580px}
.acc-video{left:680px;top:1980px;width:440px;height:262px;background:linear-gradient(150deg,#9bb98a,#4b6b3c)}
.acc-frame{left:700px;top:1960px;width:440px;height:262px;border:6px solid var(--green)}
.play{left:875px;top:2086px}

.why{left:0;top:2356px;width:1200px;height:684px;background:linear-gradient(180deg,#2f5f9e,#3f7a8a 55%,#4d7f3a)}
.why .veil{position:absolute;inset:0;background:rgba(40,90,160,.45)}
.why h2{position:absolute;left:0;width:1200px;top:60px;text-align:center;color:#fff;font-size:40px;font-weight:700}
.why p.lead{position:absolute;left:400px;width:400px;top:122px;text-align:center;color:#fff;font-size:14px;line-height:1.5}
.card{position:absolute;width:510px;height:160px;background:#fff;padding:38px 30px 0 100px}
.card svg{position:absolute;left:28px;top:42px}
.card h3{font-size:20px;font-weight:700;color:var(--ink)}
.card p{font-size:14px;color:var(--muted);line-height:1.5;margin-top:10px}

.blog-title{left:0;top:3072px;width:1200px;text-align:center;color:var(--green);font-size:38px;font-weight:700}
.post{position:absolute;top:3140px;width:310px;height:290px;color:#fff}
.post .pic{position:absolute;inset:0}
.post .cap{position:absolute;left:0;right:0;bottom:0;padding:14px 18px;background:linear-gradient(0deg,rgba(0,0,0,.75),rgba(0,0,0,0))}
.post h4{font-size:17px;font-weight:700}
.post p{font-size:13px;line-height:1.4;margin-top:4px}
.post small{font-size:11px;opacity:.8}
.chev{position:absolute;top:3260px}

.sub{left:80px;top:3510px;width:460px}
.sub p{font-size:15px;color:var(--ink);line-height:1.5;margin-top:16px}
.field{background:#ececec;border-radius:18px;height:38px;font-size:13px;color:#888;padding:11px 18px}
.divider{left:600px;top:3510px;width:1px;height:320px;background:#ddd}
.contact{left:650px;top:3510px;width:460px}

.footer{left:0;top:3940px;width:1200px;height:320px;background:var(--footer);color:#fff}
.footer h5{color:var(--green);font-size:14px;font-weight:700;margin-bottom:14px;text-transform:uppercase}
.footer ul{list-style:none}
.footer li{font-size:14px;margin-bottom:12px}
.copyright{left:0;top:4260px;width:1200px;height:48px;background:var(--footer-base);color:#fff;font-size:13px;text-align:center;line-height:48px;border-top:1px solid #222}
.pay{display:flex;gap:8px}
.pay span{width:34px;height:22px;border-radius:3px;background:#4a4a4a}
</style>
</head>
<body>

<div class="abs topbar">
  <span>Welcome Our Website</span>
  <nav><span>My Account</span><span>Gift Certificates</span><span>Wish lists</span></nav>
</div>

<header class="abs header">
  <div class="brand"><span class="dot"></span>Tulvo Brenner</div>
  <nav class="mainnav">
    <a class="active">Home</a><a>About Us</a><a>Products</a><a>Shop</a><a>Blog</a><a>Contact Us</a>
  </nav>
  <div class="social"><span></span><span></span><span></span><span></span><span></span></div>
</header>

<section class="abs hero" role="img" aria-label="Photo of a grower tending leafy plants in a greenhouse">
  <div class="shade"></div>
</section>
<div class="abs hero-text">
  <div class="small">WELCOME FOR</div>
  <div class="big">TULVO BRENNER</div>
  <div class="buy">BUY NOW</div>
</div>
<div class="abs dots"><span></span><span></span></div>

<div class="abs clone-img" role="img" aria-label="Photo of young seedlings rooting in a cloning tray">
  <span class="arrow-l"></span><span class="arrow-r"></span>
</div>
<div class="abs clone-copy">
  <h2 class="title">Tulvo Brenner Cloners</h2>
  <ul class="bullets">
    <li>Specifically designed for rapid cloning and to seed germination.</li>
    <li>Our patented technology provides a cool, constant mist of air and water for fast, consistent propagation in cloning.</li>
    <li>Say goodbye to troubles of the past. No more water pumps, air stones, clogging mister heads, sprayers, and leaky net pots. All those problems have been solved with our innovative line of cloners.</li>
    <li>Tulvo Brenner is focused on Growing Solutions that make your experience as simple and effective as possible.</li>
  </ul>
  <span class="btn" style="margin-top:4px">Shop Now</span>
</div>

<div class="abs gallery">
  <div class="g1" role="img" aria-label="Photo of seedlings in a grow tray"></div>
  <div class="g2" role="img" aria-label="Photo of aeroponic plant roots">
    <div class="over">
      <svg width="40" height="40" viewBox="0 0 40 40"><circle cx="20" cy="20" r="18" fill="#fff"/><circle cx="20" cy="20" r="7" fill="#6cbf45"/></svg>
      AEROPONICS
    </div>
  </div>
  <div class="g3" role="img" aria-label="Photo of a greenhouse interior"></div>
  <div class="g4" role="img" aria-label="Photo of herbs growing in rows"></div>
  <div class="g5" role="img" aria-label="Photo of hands holding a young plant"></div>
</div>

<h2 class="abs title acc-title">TulvoBrenners, VeldaCaps, and<br>Growing Accessories</h2>
<div class="abs acc-copy">
  <ul class="bullets">
    <li>Our Tulvo Brenner products are specifically designed to solve issues in the Hydroculture industry.</li>
    <li>We take extra time in engineering to make sure our products are the most effective, simplest to use and understand, and easiest to clean and maintain.</li>
    <li>For the products we carry but didn't design, we take care to keep vendors and products to find the best and then use innovative negotiating techniques to give you the best value without compromise of quality.</li>
    <li>One-stop shop, Tulvo Brenner is beside you and leading the Growing Revolution!</li>
  </ul>
  <span class="btn">Shop Now</span>
</div>
<div class="abs acc-frame"></div>
<div class="abs acc-video" role="img" aria-label="Video still of a greenhouse with plants"></div>
<svg class="abs play" width="50" height="50" viewBox="0 0 50 50"><circle cx="25" cy="25" r="24" fill="#fff"/><path d="M20 15 L35 25 L20 35Z" fill="#333"/></svg>

<section class="abs why" role="img" aria-label="Background photo of vegetables in a garden bed">
  <div class="veil"></div>
  <h2>Why Choose Us</h2>
  <p class="lead">Lorem Ipsum is simply dummy text of the printing and typesetting industry. Lorem Ipsum has been the industry's standard dummy text ever.</p>
  <div class="card" style="left:64px;top:236px">
    <svg width="44" height="44" viewBox="0 0 44 44"><path d="M6 38 C6 14 22 6 40 6 C40 26 30 38 6 38Z" fill="#6cbf45"/><path d="M6 38 L28 16" stroke="#fff" stroke-width="2"/></svg>
    <h3>100% Fresh Foods</h3>
    <p>Lorem Ipsum is simply dummy text of the printing and typesetting industry.</p>
  </div>
  <div class="card" style="left:626px;top:236px">
    <svg width="44" height="44" viewBox="0 0 44 44"><path d="M38 6 C26 6 16 14 12 26 L18 32 C30 28 38 18 38 6Z" fill="#6cbf45"/><path d="M12 26 L4 28 L10 20Z M18 32 L16 40 L24 34Z" fill="#6cbf45"/></svg>
    <h3>Hydroponic Vegetable</h3>
    <p>Lorem Ipsum is simply dummy text of the printing and typesetting industry.</p>
  </div>
  <div class="card" style="left:64px;top:424px">
    <svg width="44" height="44" viewBox="0 0 44 44"><rect x="2" y="12" width="24" height="18" fill="#6cbf45"/><path d="M26 18 H34 L40 24 V30 H26Z" fill="#6cbf45"/><circle cx="10" cy="33" r="4" fill="#6cbf45"/><circle cx="33" cy="33" r="4" fill="#6cbf45"/></svg>
    <h3>Home Delivery</h3>
    <p>Lorem Ipsum is simply dummy text of the printing and typesetting industry.</p>
  </div>
  <div class="card" style="left:626px;top:424px">
    <svg width="44" height="44" viewBox="0 0 44 44"><rect x="2" y="12" width="40" height="22" rx="2" fill="#6cbf45"/><circle cx="22" cy="23" r="6" fill="#fff"/></svg>
    <h3>Cash on Delivery</h3>
    <p>Lorem Ipsum is simply dummy text of the printing and typesetting industry.</p>
  </div>
</section>

<h2 class="abs blog-title">Blog Post</h2>
<svg class="chev" style="left:64px" width="20" height="40" viewBox="0 0 20 40"><path d="M16 8 L4 20 L16 32" stroke="#222" stroke-width="4" fill="none"/></svg>
<svg class="chev" style="left:1116px" width="20" height="40" viewBox="0 0 20 40"><path d="M4 8 L16 20 L4 32" stroke="#222" stroke-width="4" fill="none"/></svg>
<article class="post" style="left:112px">
  <div class="pic" role="img" aria-label="Photo of hands planting seedlings" style="background:linear-gradient(160deg,#a9cf7a,#3f6d22)"></div>
  <div class="cap"><h4>Blog Title Will be Here</h4><p>Lorem Ipsum is simply dummy text of the printing and typesetting industry.</p><small>July 21, 2020</small></div>
</article>
<article class="post" style="left:445px">
  <div class="pic" role="img" aria-label="Photo of lettuce in a hydroponic rack" style="background:linear-gradient(160deg,#cfe3b4,#6fa043)"></div>
  <div class="cap"><h4>Blog Title Will be Here</h4><p>Lorem Ipsum is simply dummy text of the printing and typesetting industry.</p><small>July 21, 2020</small></div>
</article>
<article class="post" style="left:778px">
  <div class="pic" role="img" aria-label="Photo of a basket of fresh greens" style="background:linear-gradient(160deg,#d9c9a6,#7a9a4a)"></div>
  <div class="cap"><h4>Blog Title Will be Here</h4><p>Lorem Ipsum is simply dummy text of the printing and typesetting industry.</p><small>July 21, 2020</small></div>
</article>

<div class="abs sub">
  <h2 class="title" style="font-size:36px">Subscribe Us</h2>
  <p>Lorem Ipsum is simply dummy text of the printing and typesetting industry. Lorem Ipsum has been the industry's standard dummy text ever.</p>
  <div class="field" style="width:370px;margin-top:28px">Email</div>
  <span class="btn" style="margin:14px 0 0 260px;border-radius:20px;padding:11px 24px">Subscribe</span>
</div>
<div class="abs divider"></div>
<div class="abs contact">
  <h2 class="title" style="font-size:36px">Contact with Us</h2>
  <div class="field" style="margin-top:18px">Name</div>
  <div class="field" style="margin-top:16px">Email</div>
  <div class="field" style="margin-top:16px;height:80px;border-radius:14px">Message</div>
  <span class="btn" style="margin:16px 0 0 308px;border-radius:20px;padding:11px 26px">Send Data</span>
</div>

<footer class="abs footer">
  <div class="abs" style="left:64px;top:40px;width:280px;text-align:center">
    <div style="display:flex;gap:20px;justify-content:center">
      <svg width="70" height="70" viewBox="0 0 70 70"><circle cx="35" cy="35" r="33" fill="#2f7fc0"/></svg>
      <svg width="70" height="70" viewBox="0 0 70 70"><rect x="4" y="4" width="62" height="62" fill="#5a5a5a"/></svg>
    </div>
    <p style="font-size:14px;line-height:1.6;margin-top:26px">Our company is dedicated to providing the very best quality products and service. Happy customers is our number one goal! We strive to be the best in the industry and innovate our products.</p>
  </div>
  <div class="abs" style="left:436px;top:40px"><h5>Links</h5><ul><li>Home</li><li>About Us</li><li>Products</li><li>Shop</li><li>Blog</li><li>Contact Us</li></ul></div>
  <div class="abs" style="left:610px;top:40px"><h5>My Account</h5><ul><li>My Account</li><li>Wishlist</li><li>Order Status</li><li>View Cart</li></ul></div>
  <div class="abs" style="left:816px;top:40px;width:330px">
    <h5>Contact Us</h5>
    <ul>
      <li style="display:flex;gap:12px"><svg width="14" height="18" viewBox="0 0 14 18"><path d="M7 0 C3 0 0 3 0 7 C0 12 7 18 7 18 C7 18 14 12 14 7 C14 3 11 0 7 0Z" fill="#fff"/><circle cx="7" cy="7" r="2.5" fill="#0d0d0d"/></svg><span>Tulvo Brenner INC.<br>1180 Harlow Ave.<br>Brisbane QLD 4000</span></li>
      <li style="display:flex;gap:12px;margin-top:14px"><svg width="14" height="16" viewBox="0 0 14 16"><path d="M2 0 L5 0 L6 4 L4 6 C5 9 7 11 10 12 L12 10 L14 11 L14 14 C14 15 13 16 12 16 C5 15 0 9 0 2 C0 1 1 0 2 0Z" fill="#fff"/></svg>07-3100-4827</li>
      <li style="display:flex;gap:12px;margin-top:14px"><svg width="16" height="12" viewBox="0 0 16 12"><rect width="16" height="12" fill="#fff"/><path d="M0 0 L8 7 L16 0" stroke="#0d0d0d" fill="none"/></svg>hello@tulvobrenner.com</li>
    </ul>
    <div class="pay" style="margin-top:26px"><span></span><span></span><span></span><span></span><span></span><span></span><span></span><span></span></div>
  </div>
  <div class="abs" style="left:580px;top:276px;display:flex;gap:12px"><span style="width:26px;height:26px;background:var(--green);border-radius:3px"></span><span style="width:26px;height:26px;background:var(--green);border-radius:3px"></span><span style="width:26px;height:26px;background:var(--green);border-radius:3px"></span><span style="width:26px;height:26px;background:var(--green);border-radius:3px"></span><span style="width:26px;height:26px;background:var(--green);border-radius:3px"></span></div>
</footer>
<div class="abs copyright">Copyright © 2020 TULVO BRENNER - All Rights Reserved.</div>

</body>
</html>
```